NFC (Near field communication) - Business Card Design

IT/ Telecom:

We would like a new business card that contains our logo, contact info for the company and contact info for the owner. We also wolud like to be innovative, and create NFC technology inside the card.

This means that mobile phones can be placed on the card, and the contactinfo automaticly stores into the phonebook. Therefore, a cirkle or similar - with the text: "Place your phone here!" (please write it in Norwagian): "Aktiver NFC og legg mobilen din her!".

Please google NFC or near field communication and use your imagination on the design as we love surprises :-)

Industry/Entity Type

Communication

Requirements
Must have
• Text: "Activate NFC on your phone and place your mobile here - in Norwegian: "Aktiver NFC og legg mobilen din her!".
Nice to have
• Please see attachment #5 for inspiration.

```html
<!DOCTYPE html>
<html lang="no">
<head>
<meta charset="utf-8">
<title>linkvera – NFC business card</title>
<link rel="stylesheet" href="https://fonts.googleapis.com/css2?family=Open+Sans:wght@400;600&display=swap">
<style>
  :root {
    --backdrop: #c0c0c0;
    --brand-blue: #44788f;
    --brand-blue-soft: #c7d7df;
    --accent-orange: #ee5a24;
    --accent-orange-soft: #efc3b0;
    --ink: #1e1e1e;
    --paper: #ffffff;
  }
  * { box-sizing: border-box; margin: 0; padding: 0; }
  html, body { width: 1200px; height: 905px; overflow: hidden; }
  body {
    position: relative;
    background: var(--backdrop);
    font-family: "Open Sans", Arial, sans-serif;
  }
  .card { position: absolute; width: 655px; height: 393px; }
  .card-back { left: 151px; top: 376px; background: var(--brand-blue); }
  .card-front { left: 417px; top: 181px; background: var(--paper); }

  .brand { position: absolute; display: flex; align-items: center; }
  .brand-mark { display: block; width: 130px; height: 90px; border-radius: 12px; }
  .brand-name { font-weight: 400; letter-spacing: -1px; line-height: 1; }

  .card-front .brand { left: 36px; top: 37px; }
  .card-front .brand-mark { background: var(--brand-blue); }
  .card-front .brand-name { color: var(--brand-blue); font-size: 78px; margin-left: 20px; margin-top: -14px; }

  .card-back .brand { left: 39px; top: 272px; }
  .card-back .brand-mark { border: 2px solid var(--paper); }
  .card-back .brand-name { color: var(--paper); font-size: 78px; margin-left: 20px; margin-top: -14px; }

  .contact { position: absolute; left: 43px; top: 152px; color: var(--ink); }
  .contact-name { color: var(--accent-orange); font-size: 28px; font-weight: 400; letter-spacing: .5px; line-height: 36px; }
  .contact-role { font-size: 18px; line-height: 22px; margin-bottom: 28px; }
  .contact-list { list-style: none; font-size: 19.5px; line-height: 25.6px; }

  .nfc-zone { position: absolute; left: 403px; top: 155px; width: 225px; height: 212px; }
  .nfc-graphic {
    position: absolute; inset: 0; border-radius: 50%;
    background: radial-gradient(ellipse at center, var(--paper) 48%, var(--brand-blue-soft) 78%, var(--accent-orange-soft) 100%);
  }
  .nfc-label {
    position: absolute; left: 0; right: 0; top: 77px;
    text-align: center; font-size: 18px; line-height: 21px; color: var(--ink);
  }
</style>
</head>
<body>
  <section class="card card-back" aria-label="Card back">
    <div class="brand">
      <span class="brand-mark"></span>
      <span class="brand-name">linkvera</span>
    </div>
  </section>

  <section class="card card-front" aria-label="Card front">
    <div class="brand">
      <span class="brand-mark"></span>
      <span class="brand-name">linkvera</span>
    </div>

    <div class="contact">
      <h1 class="contact-name">MARTIN HALE</h1>
      <p class="contact-role">Director</p>
      <ul class="contact-list">
        <li>info@linkvera.nl</li>
        <li>www.linkvera.nl</li>
        <li>T: +31 35 4821907</li>
        <li>F: +31 35 4821908</li>
        <li>Postbus 12, 1400 AB Bussum</li>
      </ul>
    </div>

    <div class="nfc-zone">
      <div class="nfc-graphic" role="img" aria-label="NFC tap zone graphic: interlocking blue and orange rings"></div>
      <p class="nfc-label">Aktiver NFC og<br>legg mobilen<br>din her!</p>
    </div>
  </section>
</body>
</html>
```